Corvana Teal Outings is an Exciting Water and Land Excursions business that needs a website.

We need a website for our company. We are based in Bimini Bahamas and we sell land and sea excursions. We sell Private boat Charters, Reef Shark Snorkeling, Merloth Shipwreck Snorkeling, Stingray feeding adventures, Dolphin Tours, Sunset Cruises, Scuba Diving, Offshore Fishing, Reef Fishing, Flats Backwater Fishing, Party Island Cruise, Island Land Party Bicycle Tours, Jet Ski Tours, Guided Kayak Tours, Beach Chairs/Umbrella Rentals, Cabana Rentals, Jet Ski Rentals, Kayak Rentals, Paddle Board Rentals, Water Hammock Rentals, and Paint by the Sea Excursion

The home page will have the following tabs:
Adventures
Watersports
Photos
Alcohol
START YOUR ADVENTURE - Booking button
The adventures

We are currently using tallvex for our reservation system and that will need to be integrated with our website along with quarmona or a similar app for purchase of photos.
Updates

Need extra days to review

Target Market(s)

Our target market are tourists

Industry/Entity Type

Tourism

Coding

Coded - Design and coding required

Font styles to use
Sans Serif

Colors
0094D4
00A9DD
6FCCEA
C7EBF8
E9F6FB

Requirements
Must have
• The website must be in wordpress so we can add our external reservation system
Nice to have
• We need to have big photos and a lot of photos

```html
<!DOCTYPE html>
<html lang="en">
<head>
<meta charset="utf-8">
<title>Corvana Teal Outings — Gallery</title>
<link href="https://fonts.googleapis.com/css2?family=Bebas+Neue&family=Catamaran:wght@400;500;600;700&display=swap" rel="stylesheet">
<style>
:root{
  --indigo:#29259f;
  --brand:#1f22c9;
  --accent:#1c1ce0;
  --green:#3cc13c;
  --ink:#1c1b2e;
  --body:#3a3a44;
  --nav:#5a5a66;
  --footer:#0c0a1e;
  --footer-text:#8c8ca4;
  --white:#ffffff;
}
*{margin:0;padding:0;box-sizing:border-box}
html,body{width:673px;height:1200px;overflow:hidden;background:var(--white)}
body{position:relative;font-family:"Catamaran",sans-serif;color:var(--body)}
.abs{position:absolute}
.topbar{left:0;top:0;width:673px;height:22px;background:var(--indigo);color:var(--white);font-size:9px}
.social-dot{width:8px;height:8px;border-radius:50%;background:var(--white);top:7px}
.topbar .contact{top:4px;display:flex;align-items:center;gap:6px;line-height:14px}
.topbar .sep{left:497px;top:6px;width:1px;height:10px;background:rgba(255,255,255,.6)}
.header{left:0;top:22px;width:673px;height:46px;background:var(--white)}
.logo{left:45px;top:34px;display:flex;align-items:center;gap:6px;font-weight:700;font-size:12px;color:var(--brand);letter-spacing:.5px;text-transform:uppercase}
.logo .mark{width:22px;height:22px;background:var(--green)}
.nav{top:38px;font-size:9.2px;font-weight:600;color:var(--nav);letter-spacing:.2px}
.nav.active{color:var(--indigo)}
.nav-dots{left:451px;top:52px;display:flex;gap:2px}
.nav-dots span{width:2px;height:2px;border-radius:50%;background:var(--accent)}
.book{left:535px;top:32px;width:85px;height:24px;background:var(--green);color:var(--white);font-size:8.6px;font-weight:700;display:flex;align-items:center;justify-content:center;letter-spacing:.3px}
.hero{left:0;top:68px;width:673px;height:159px;background:linear-gradient(180deg,#3f8fd8 0%,#8cc3ee 45%,#1c8fb0 62%,#2fa6b6 100%)}
.title{left:0;top:272px;width:673px;text-align:center;font-family:"Bebas Neue",sans-serif;font-size:30px;color:var(--ink);letter-spacing:.3px}
.title-rule{left:319px;top:308px;width:36px;height:2px;background:var(--accent)}
.intro{left:150px;top:322px;width:373px;text-align:center;font-size:10.2px;line-height:18px;color:var(--body)}
.tile{overflow:hidden}
.caption-wrap{left:250px;top:521px;width:199px;height:226px;background:rgba(6,40,60,.35)}
.zoom{left:333px;top:659px;width:32px;height:32px;border-radius:50%;background:var(--green)}
.caption{left:250px;top:706px;width:199px;text-align:center;font-family:"Bebas Neue",sans-serif;font-size:16.5px;color:var(--white);letter-spacing:.1px}
.footer-bg{left:0;top:905px}
.fh{top:992px;font-family:"Bebas Neue",sans-serif;font-size:16px;color:var(--white);letter-spacing:.2px}
.ftext{font-size:9.4px;line-height:18px;color:var(--footer-text)}
.fsocial{width:8px;height:8px;border-radius:50%;background:var(--white);top:1105px}
.cbox{left:446px;width:26px;height:26px;background:var(--green);display:flex;align-items:center;justify-content:center}
.copyright{left:0;top:1166px;width:673px;text-align:center;font-size:8.4px;letter-spacing:.6px;color:var(--footer-text)}
</style>
</head>
<body>

<div class="abs topbar"></div>
<span class="abs social-dot" style="left:44px"></span>
<span class="abs social-dot" style="left:62px"></span>
<span class="abs social-dot" style="left:82px"></span>
<div class="abs topbar contact" style="left:403px;width:auto;height:auto;background:none">
  <svg width="10" height="10" viewBox="0 0 24 24" fill="#fff"><path d="M6.6 10.8a15.1 15.1 0 0 0 6.6 6.6l2.2-2.2a1 1 0 0 1 1-.25 11.4 11.4 0 0 0 3.6.57 1 1 0 0 1 1 1V20a1 1 0 0 1-1 1A17 17 0 0 1 3 4a1 1 0 0 1 1-1h3.5a1 1 0 0 1 1 1c0 1.25.2 2.45.57 3.57a1 1 0 0 1-.25 1z"/></svg>
  <span>123-456-7890</span>
</div>
<span class="abs sep topbar" style="left:497px;top:6px;width:1px;height:10px;background:rgba(255,255,255,.6)"></span>
<div class="abs topbar contact" style="left:514px;width:auto;height:auto;background:none">
  <svg width="10" height="10" viewBox="0 0 24 24" fill="#fff"><path d="M2 9l10-6 10 6v11H2z"/><path d="M4 10l8 5 8-5" stroke="#29259f" stroke-width="1.6" fill="none"/></svg>
  <span>info@corvanateal.com</span>
</div>

<div class="abs header"></div>
<div class="abs logo"><span class="mark"></span>Corvana Teal Outings</div>
<span class="abs nav" style="left:267px">HOME</span>
<span class="abs nav" style="left:303px">OUR ADVENTURES</span>
<span class="abs nav" style="left:391px">RENTALS</span>
<span class="abs nav active" style="left:438px">GALLERY</span>
<div class="abs nav-dots"><span></span><span></span><span></span></div>
<span class="abs nav" style="left:485px">CONTACT</span>
<div class="abs book">BOOK NOW</div>

<div class="abs hero" role="img" aria-label="Rusted shipwreck standing in turquoise sea under a blue sky"></div>

<h1 class="abs title">GALLERY</h1>
<div class="abs title-rule"></div>
<p class="abs intro">Quis nostrud exercitation ullamco laboris nisi ut aliquip ex ea commodo consequat. Duis aute irur dolor in reprehenderit in voluptate velit esse cillu dolore eu fugiat nulla pariatur.</p>

<div class="abs tile" role="img" aria-label="Guides on the beach with jet skis and kayaks" style="left:45px;top:405px;width:199px;height:226px;background:linear-gradient(180deg,#3b86c8 0%,#1fa3c9 40%,#d8d0c0 70%,#e86a3a 100%)"></div>
<div class="abs tile" role="img" aria-label="Angler releasing a fish beside the boat" style="left:250px;top:405px;width:199px;height:110px;background:linear-gradient(120deg,#d8dde2 0%,#2fb592 45%,#27b9a0 100%)"></div>
<div class="abs tile" role="img" aria-label="White charter boat at the dock" style="left:455px;top:405px;width:165px;height:110px;background:linear-gradient(180deg,#5d9ad8 0%,#9ac3e8 30%,#e8ecef 60%,#2f6f9c 100%)"></div>
<div class="abs tile" role="img" aria-label="Snorkelers swimming in deep blue water" style="left:250px;top:521px;width:199px;height:226px;background:linear-gradient(180deg,#1d5a72 0%,#19516a 60%,#123e55 100%)"></div>
<div class="abs tile" role="img" aria-label="Party bicycle with coloured lights" style="left:455px;top:521px;width:165px;height:110px;background:linear-gradient(180deg,#8a7a70 0%,#4d8fb0 50%,#3c3a48 100%)"></div>
<div class="abs tile" role="img" aria-label="Angler holding a large fish over turquoise water" style="left:45px;top:637px;width:199px;height:110px;background:linear-gradient(90deg,#e6e4e2 0%,#5cc2b4 50%,#44b8b0 100%)"></div>
<div class="abs tile" role="img" aria-label="Aerial view of beach with umbrellas" style="left:455px;top:637px;width:165px;height:110px;background:linear-gradient(110deg,#e4e2dc 0%,#d6d8da 45%,#43c6cc 75%,#1aa8c8 100%)"></div>
<div class="abs tile" role="img" aria-label="Racks of yellow kayaks on the sand" style="left:45px;top:753px;width:199px;height:110px;background:linear-gradient(180deg,#6a9fd6 0%,#5a7a50 30%,#e2a020 60%,#ddd6ca 100%)"></div>
<div class="abs tile" role="img" aria-label="Centre console boat moored at marina" style="left:250px;top:753px;width:199px;height:110px;background:linear-gradient(180deg,#7fa8d6 0%,#486c7c 35%,#e4e6e6 60%,#2a4a5c 100%)"></div>
<div class="abs tile" role="img" aria-label="Beach cabana with lounge chairs" style="left:455px;top:753px;width:165px;height:110px;background:linear-gradient(180deg,#7aa5d4 0%,#5ea8c4 35%,#dcd6cc 65%,#eceae6 100%)"></div>

<div class="abs caption-wrap"></div>
<div class="abs zoom">
  <svg width="32" height="32" viewBox="0 0 32 32"><circle cx="15" cy="15" r="6" fill="none" stroke="#fff" stroke-width="1.8"/><path d="M19.4 19.4l4 4M15 12v6M12 15h6" stroke="#fff" stroke-width="1.8" stroke-linecap="round"/></svg>
</div>
<div class="abs caption">REEF SHARK SNORKELING TOURS</div>

<svg class="abs footer-bg" width="673" height="295" viewBox="0 0 673 295"><polygon points="0,0 673,57 673,295 0,295" fill="#0c0a1e"/></svg>

<h3 class="abs fh" style="left:45px">ABOUT US</h3>
<p class="abs ftext" style="left:45px;top:1018px;width:200px">Lorem ipsum dolor sit amet, consecteturot adipisicings elit, sed do eiusmod tempor al incididunt ut labore et dolore magna aute aliquat enim ad minim veniam,aliquip ex.</p>
<span class="abs fsocial" style="left:44px"></span>
<span class="abs fsocial" style="left:62px"></span>
<span class="abs fsocial" style="left:82px"></span>

<h3 class="abs fh" style="left:309px">QUICK LINKS</h3>
<div class="abs ftext" style="left:310px;top:1018px">Home<br>Adventures<br>Watersports<br>Gallery<br>Contact</div>

<h3 class="abs fh" style="left:445px">CONTACT INFORMATION</h3>
<div class="abs cbox" style="top:1024px"><svg width="10" height="12" viewBox="0 0 20 24"><path d="M10 1a8 8 0 0 0-8 8c0 6 8 14 8 14s8-8 8-14a8 8 0 0 0-8-8z" fill="#fff"/><circle cx="10" cy="9" r="3" fill="#3cc13c"/></svg></div>
<div class="abs ftext" style="left:484px;top:1019px;width:140px;line-height:16px">labore et dolore magna aute eniam,aliqu</div>
<div class="abs cbox" style="top:1061px"><svg width="10" height="10" viewBox="0 0 24 24" fill="#fff"><path d="M6.6 10.8a15.1 15.1 0 0 0 6.6 6.6l2.2-2.2a1 1 0 0 1 1-.25 11.4 11.4 0 0 0 3.6.57 1 1 0 0 1 1 1V20a1 1 0 0 1-1 1A17 17 0 0 1 3 4a1 1 0 0 1 1-1h3.5a1 1 0 0 1 1 1c0 1.25.2 2.45.57 3.57a1 1 0 0 1-.25 1z"/></svg></div>
<div class="abs ftext" style="left:484px;top:1056px;line-height:16px">Phone:<br>123-456-7890</div>
<div class="abs cbox" style="top:1097px"><svg width="11" height="11" viewBox="0 0 24 24"><path d="M2 9l10-6 10 6v11H2z" fill="#fff"/><path d="M4 10l8 5 8-5" stroke="#3cc13c" stroke-width="1.6" fill="none"/></svg></div>
<div class="abs ftext" style="left:484px;top:1092px;line-height:16px">Email:<br>info@corvanateal.com</div>

<p class="abs copyright">COPYRIGHT © 2022 CORVANA TEAL OUTINGS. ALL RIGHTS RESERVED.</p>

</body>
</html>
```